【 概要 】 起業塾メディアサイトのメインバナーのデザイン作成をお願いします。 【 依頼内容 】 ・サイズ: 横2300 × 縦1200px ・作成数: 1種類 【 デザインイメージ 】 ・ターゲット層:起業塾の利用検討者向け ・雰囲気:リアルな実体験が載っていそうな雰囲気 【 使用素材 】 (使用テキスト) 最新2023年の起業塾の徹底比較、評判まとめサイトの決定版 現役起業家が100人以上へのアンケート実施や潜入体験レポート。1サービス平均10時間以上の徹底調査 (使用画像) フリー素材を使いつつも、フリー素材に見えにくい形だと助かります。 |
文字の視認性が高く、イラスト風なデザインも好みだったので採用させていただきました!
皆さん、ご提案ありがとうございました!またの機会がありましたら応募させていただきますので、よろしくお願いします!

```html
<!DOCTYPE html>
<html lang="ja">
<head>
<meta charset="UTF-8">
<title>起業塾 徹底比較 メインバナー</title>
<link rel="stylesheet" href="https://fonts.googleapis.com/css2?family=Noto+Sans+JP:wght@700;900&family=Noto+Serif+JP:wght@600;700&display=swap">
<style>
  :root {
    --navy: #1b2350;
    --navy-edge: #2c3770;
    --white: #ffffff;
    --band: rgba(18, 18, 22, 0.86);
    --band-edge: rgba(18, 18, 22, 0.55);
    --photo-top: #9aa0a8;
    --photo-mid: #3c3f46;
    --photo-low: #1c1d22;
    --table: #5c5f66;
  }
  * { margin: 0; padding: 0; box-sizing: border-box; }
  html, body { width: 1200px; height: 626px; overflow: hidden; background: #222; }
  .banner {
    position: relative;
    width: 1200px;
    height: 626px;
    overflow: hidden;
  }
  .scene-photo {
    position: absolute;
    inset: 0;
    background:
      radial-gradient(ellipse at 50% 10%, rgba(235,238,242,0.55), transparent 55%),
      linear-gradient(180deg, var(--photo-top) 0%, var(--photo-mid) 45%, var(--photo-low) 70%, var(--table) 100%);
  }
  .dark-band {
    position: absolute;
    left: 0; right: 0;
    top: 110px;
    height: 410px;
    background: linear-gradient(180deg, var(--band-edge) 0%, var(--band) 12%, var(--band) 88%, var(--band-edge) 100%);
  }
  .content {
    position: absolute;
    inset: 0;
    display: flex;
    flex-direction: column;
    align-items: center;
  }
  .kicker {
    position: relative;
    margin-top: 144px;
    width: 620px;
    height: 60px;
    display: flex;
    align-items: center;
    justify-content: center;
    gap: 6px;
    font-family: "Noto Sans JP", sans-serif;
    font-weight: 700;
    font-size: 29px;
    color: var(--white);
    letter-spacing: 0.04em;
  }
  .kicker-shape { position: absolute; inset: 0; z-index: 0; }
  .kicker-text { position: relative; z-index: 1; }
  .kicker-box {
    position: relative;
    z-index: 1;
    display: inline-block;
    width: 40px;
    height: 40px;
    line-height: 38px;
    text-align: center;
    background: var(--white);
    color: var(--navy);
    font-weight: 900;
    font-size: 30px;
    margin-left: 2px;
  }
  .headline {
    margin-top: 26px;
    font-family: "Noto Serif JP", serif;
    font-weight: 600;
    font-size: 86px;
    line-height: 1.2;
    color: var(--white);
    letter-spacing: 0.01em;
    text-shadow: 0 0 18px rgba(255,255,255,0.35);
  }
  .lead {
    margin-top: 28px;
    font-family: "Noto Serif JP", serif;
    font-weight: 700;
    font-size: 26px;
    line-height: 1.7;
    color: var(--white);
    text-align: center;
    letter-spacing: 0.02em;
  }
</style>
</head>
<body>
  <div class="banner">
    <div class="scene-photo" role="img" aria-label="会議室でテーブルを挟んで話し合うビジネスパーソンの写真"></div>
    <div class="dark-band"></div>
    <div class="content">
      <div class="kicker">
        <svg class="kicker-shape" viewBox="0 0 620 60" preserveAspectRatio="none" aria-hidden="true">
          <polygon points="14,0 606,0 620,30 606,60 14,60 0,30" fill="var(--navy)" stroke="var(--navy-edge)" stroke-width="2"/>
        </svg>
        <span class="kicker-text">最新2023年の起業塾の</span>
        <span class="kicker-box">徹</span><span class="kicker-box">底</span><span class="kicker-box">比</span><span class="kicker-box">較</span>
      </div>
      <h1 class="headline">評判まとめサイトの決定版</h1>
      <p class="lead">現役起業家が100人以上へのアンケート実施や潜入体験レポート<br>1サービス平均10時間以上の徹底調査</p>
    </div>
  </div>
</body>
</html>
```